Label for Wines Design

I need a label design for a start-up business that makes grape wines. The label of wine features a picture frame on the edges of the wine bottle label. So each style of wine (red, white, sparkling, rose etc) will feature a different colour. As you can picture there is already a lot going on in this label.

My trademark is 'tamo', means 'Virgin pure love',type of wines: Sauvignon Blanc, Merlot, Pino noir etc. All in Caps, a Juxtaposition of old & modern. Bold & thick letters to grab attention on the wine store shelves. Maybe letter spacing squeezed together as the wine label is only 4inches wide...the text 'tamo' must fit on one line! No Cursive or curvy lines! Colors open to black, green, yellow, purple must be natural colors hues in nature.

New Zealand wines are New worlds wines,green and astringency,unique fruity, just as virgin pure love, is an infatuation, lovesickness, never forget......

Target Market(s)

New Zealand and Asian
food & wine lovers all ages

Industry/Entity Type

Business

Font styles to use
Decorative
Script

Colors

Designer to choose colors to be used in the design.

Requirements
Must have
• Front Label and back label
Nice to have
• Wines-feeling is green and astringency,unique fruity, just as virgin pure love, is an infatuation, lovesickness, never forget......

```html
<!DOCTYPE html>
<html lang="en">
<head>
<meta charset="utf-8">
<title>TAMO Sauvignon Blanc – Front Label</title>
<link rel="stylesheet" href="https://fonts.googleapis.com/css2?family=Playfair+Display:wght@400&family=Montserrat:wght@500&display=swap">
<style>
  :root {
    --canvas: #f4f3f0;
    --label-white: #f7f7f6;
    --ink: #2b2b2d;
    --ink-soft: #4a4a4c;
    --haze: #d9d6d2;
    --hill: #a7a1a4;
    --vine-green: #5f7640;
    --vine-shadow: #3b3648;
    --grass: #8ea06a;
  }
  * { margin: 0; padding: 0; box-sizing: border-box; }
  html, body {
    width: 939px; height: 1200px; overflow: hidden;
    background: var(--canvas);
  }
  .canvas {
    position: relative; width: 939px; height: 1200px;
    display: flex; align-items: center; justify-content: center;
  }
  .front-label {
    position: relative; width: 840px; height: 860px;
    background: var(--label-white);
    box-shadow: 0 2px 10px rgba(0,0,0,0.08);
    overflow: hidden;
  }
  .masthead {
    height: 305px;
    display: flex; flex-direction: column;
    align-items: center; justify-content: center;
    gap: 18px;
  }
  .wordmark {
    font-family: "Playfair Display", Georgia, serif;
    font-weight: 400; font-size: 168px; line-height: 1;
    letter-spacing: 0.02em; color: var(--ink);
  }
  .tagline {
    font-family: "Montserrat", Arial, sans-serif;
    font-weight: 500; font-size: 15px; letter-spacing: 0.3em;
    color: var(--ink-soft);
  }
  .vineyard-photo {
    height: 400px;
    background:
      linear-gradient(180deg, var(--haze) 0%, var(--hill) 32%, var(--haze) 42%, var(--vine-green) 58%, var(--vine-shadow) 74%, var(--grass) 88%, var(--vine-green) 100%);
  }
  .varietal-band {
    height: 155px;
    padding: 36px 48px 0 44px;
    display: flex; justify-content: space-between; align-items: flex-start;
  }
  .varietal-name {
    font-family: "Playfair Display", Georgia, serif;
    font-weight: 400; font-size: 40px; line-height: 1.2; color: var(--ink);
    padding-bottom: 10px; border-bottom: 1.5px solid var(--ink-soft);
  }
  .origin {
    margin-top: 12px;
    font-family: "Montserrat", Arial, sans-serif;
    font-weight: 500; font-size: 15px; letter-spacing: 0.16em;
    color: var(--ink-soft);
  }
  .vintage {
    margin-top: 14px;
    font-family: "Playfair Display", Georgia, serif;
    font-weight: 400; font-size: 62px; line-height: 1; color: var(--ink);
    font-variant-numeric: lining-nums;
  }
</style>
</head>
<body>
  <main class="canvas">
    <section class="front-label">
      <header class="masthead">
        <h1 class="wordmark">TAMO</h1>
        <p class="tagline">UNIQUE FRUITY</p>
      </header>
      <div class="vineyard-photo" role="img" aria-label="Vineyard rows at dusk under hazy hills with a lone tree"></div>
      <footer class="varietal-band">
        <div class="varietal">
          <h2 class="varietal-name">Sauvignon Blanc</h2>
          <p class="origin">NEW ZEALAND WINE</p>
        </div>
        <p class="vintage">2017</p>
      </footer>
    </section>
  </main>
</body>
</html>
```